Website redesign for a Cloud Advisory business

We are looking to revisit our existing brand and website, with a view to updating both. Looking for concepts and designs for how the website might look, flow and feel. Current website is: www.brellomint.com.au

Scope and Deliverables: Concept design for the home page and one internal page.

We do not expect you to design all the pages and all the elements of the website at this stage.

This job is not for the full website design, but just for concepts that we can start with when we go into the full website design.

We would love to see a design feature based on our name, logo, or industry, which can run through banners and other collateral (twitter banner, ads on Google, corporate documents etc).

We want the brand to properly depict what we bring/deliver to businesses when consulting to them and this should extend to the colour scheme, logo, font (perhaps updated) and copy (which will be supplied).

Our brand should suitably communicate our ability, knowledge and extensive experience within the Cloud space.

It should express and evoke credibility, knowledge and understanding of the Cloud space, independence, gravitas, reliability, efficiency, trust, expertise, approachability, service delivery but be uncomplicated, practical and use plain speaking language.

Colours that reinforce this might include: Blues, blacks, silver, white, grey and our existing orange.

Website designs that we like or have referenced include:

Varnolift: http://varnolift.com.au/ - This has good information but looks a little amateur in it’s cartoon like design and colour scheme. Also, this seems to be aimed at clients more interested in price than design and what we are going for is a little more high end.

Pendramoor: https://www.pendramoor.com.au/ - This site has merit in its’ setup but little call to action on the home page, especially before the scroll line. I like the set up of the Case Studies page however I’d look to make it more prominent by having it set up 3 across rather than the 4 they have. Something such as this: https://www.qandelby.com/case-studies

Tolvane: http://www.tolvane.com.au/#home4 - This page is a good one as far as selling services and information on the company. I quite like it.

MirefoldIT: http://www.mirefoldit.com.au/ - While I don’t think is particularly creative, it does practically depict the services we offer in a fairly clear way and might be a bit of a basic (albeit dull) template to follow.

JDP: https://store.jdp.com/us/Product-Family/JDP-Advisory-Services/JDP-Cloud-Advisory-Service/p/JDP-Services-Cloud-Advisory - This offers substantial information but is probably a little confusing although the roll-over drop down menus have merit.

ZEV: http://www.zev.net.au/en/services/ - While this in not quite what we are looking for, the colour scheme gives it more gravitas and quality.

As another reference, this website and the way they present their case studies is also something we like, although I’d like them shown 3 up, side by side…. https://www.qandelby.com/case-studies.

We have added a page layout and page purpose document.

Target Market(s)

Corporates, small - medium business, direct referrals, via search results

Industry/Entity Type

Business

Number of Pages Required

1 page

Font styles to use
Sans Serif

Colors
85abd2
0455a3
000000
f37122
5c5c5c

Requirements
Must have
• Website must be mobile device compatible.
• Concept design for the home page.
Nice to have
• We would love to see a design feature based on our name, logo, or industry, which can run through banners and other collateral (twitter banner, ads on Google, corporate documents etc).

```html
<!DOCTYPE html>
<html lang="en">
<head>
<meta charset="utf-8">
<title>Brellomint – Impartial Cloud Solutions</title>
<link href="https://fonts.googleapis.com/css2?family=Montserrat:wght@400;600;700&family=Arimo:wght@400;700&family=Open+Sans:ital,wght@1,400&family=Roboto+Condensed:wght@400&display=swap" rel="stylesheet">
<style>
:root{
  --orange:#f7931e;
  --orange-deep:#f37122;
  --orange-dark:#7a3d0a;
  --ink:#1a1a1a;
  --grey:#5c5c5c;
  --grey-mid:#8a8a8a;
  --grey-light:#e6e7e8;
  --nav:#efefef;
  --blue-dark:#0b2744;
  --blue:#0455a3;
  --blue-soft:#85abd2;
  --white:#ffffff;
}
*{box-sizing:border-box;margin:0;padding:0}
html,body{width:795px;height:1200px;overflow:hidden;background:var(--white)}
body{position:relative;font-family:"Arimo",Arial,sans-serif;color:var(--grey)}
.abs{position:absolute}

/* hero */
.hero-photo{left:41px;top:14px;width:713px;height:300px;
  background:radial-gradient(ellipse at 60% 40%,#3fa9e0 0%,#16578f 35%,#0b2744 70%,#0a1626 100%)}
.brand{left:41px;top:28px;width:138px;height:34px;background:var(--white);border-radius:0 17px 17px 0;
  display:flex;align-items:center;gap:5px;padding-left:6px}
.brand-mark{width:10px;height:10px;background:var(--orange-deep)}
.brand-name{font-family:"Montserrat",sans-serif;font-weight:600;font-size:12px;color:var(--orange-deep);letter-spacing:.5px}
.account{left:678px;top:20px;width:63px;height:17px;border:1.5px solid var(--orange);
  color:var(--white);font-size:6.5px;display:flex;align-items:center;justify-content:center;gap:4px}
.hero-title{left:81px;top:96px;font-family:"Montserrat",sans-serif;font-weight:600;font-size:42px;line-height:38px;color:var(--white);letter-spacing:-.5px}
.hero-sub{left:82px;top:214px;font-family:"Montserrat",sans-serif;font-size:11.2px;line-height:13.5px;color:var(--white)}
.hero-cta{left:82px;top:253px;width:224px;height:34px;border-radius:17px;background:var(--orange);
  color:var(--white);font-family:"Montserrat",sans-serif;font-weight:700;font-size:16px;display:flex;align-items:center;justify-content:center}

/* nav */
.main-nav{left:41px;top:314px;width:713px;height:23px;background:var(--nav)}
.nav-item{top:320px;font-size:9px;color:var(--grey)}
.nav-search{left:669px;top:317px;font-size:12px;color:var(--grey)}

/* testimonial */
.testimonial-photo{left:41px;top:337px;width:713px;height:122px;
  background:linear-gradient(180deg,#c9cacc,#a9abae);
  clip-path:polygon(0 0,100% 0,100% 85%,57% 85%,50% 100%,43% 85%,0 85%)}
.client-badge{left:357px;top:357px;width:69px;height:30px;background:var(--white);border-radius:4px;
  display:flex;align-items:center;justify-content:center;font-family:"Montserrat",sans-serif;font-weight:600;font-size:7.5px;color:#c8102e}
.quote{left:180px;top:397px;width:430px;text-align:center;font-family:"Open Sans",sans-serif;font-style:italic;font-size:7px;line-height:9.8px;color:var(--ink)}
.quote-arrow{top:391px}

/* about */
.section-title{font-size:26px;color:var(--grey);width:795px;left:0;text-align:center}
.about-block{width:178px}
.about-block h3{font-weight:400;font-size:13px;color:var(--orange);margin-bottom:6px}
.about-block p{font-size:11.5px;line-height:13.8px;text-align:justify;text-align-last:left;color:var(--grey-mid)}
.read-more{display:block;margin-left:auto;width:53px;margin-top:3px;border:1px solid var(--orange);color:var(--orange);font-size:9.5px;text-align:center;line-height:10px}
.about-cta{left:312px;top:641px;width:173px;height:46px;background:var(--orange);border:1.5px solid var(--orange);outline:1px solid var(--white);outline-offset:-3px;
  text-align:center;font-family:"Montserrat",sans-serif;font-weight:700;font-size:18px;line-height:19px;padding-top:4px;color:var(--white)}
.about-cta .soft{color:var(--orange-dark)}
.about-cta .dark{color:var(--ink)}

/* banner */
.promo{left:41px;top:706px;width:713px;height:82px;border-top:1px solid var(--orange);border-bottom:1px solid var(--orange);
  background:linear-gradient(90deg,#c8cdd2,#dfe4e8 45%,#d4dde3)}
.promo-title{left:0;width:795px;top:728px;text-align:center;font-family:"Montserrat",sans-serif;font-weight:700;font-size:24px;color:var(--ink);letter-spacing:.5px}
.promo-sub{left:0;width:795px;top:760px;text-align:center;font-family:"Open Sans",sans-serif;font-style:italic;font-size:7.5px;color:var(--ink)}

/* contact */
.world-map{left:60px;top:815px;width:640px;height:300px;background:radial-gradient(ellipse at 50% 45%,#e4e4e4 0%,#f1f1f1 55%,#fff 80%)}
.field{left:92px;width:284px;border:1.5px solid #b3b3b3;background:rgba(255,255,255,.85);font-size:13px;color:#a6a6a6;padding:6px 9px}
.copy-check{left:92px;top:1027px;width:13px;height:13px;border:1.5px solid #a6a6a6;border-radius:2px;background:var(--white)}
.copy-label{left:110px;top:1028px;font-family:"Open Sans",sans-serif;font-style:italic;font-size:7px;color:var(--grey)}
.send{left:273px;top:1047px;width:103px;height:22px;background:var(--orange);color:#fde0b8;font-size:12px;display:flex;align-items:center;justify-content:center}
.divider{left:397px;top:829px;width:1px;height:238px;background:#b3b3b3}
.contact-info{left:485px;top:888px;font-family:"Roboto Condensed",sans-serif;font-size:13px;line-height:17.5px;color:var(--ink)}

.social-link{font-family:"Arimo",sans-serif;font-weight:700;color:var(--orange)}
.social-link.large{top:965px;font-size:13px}
.social-link.small{top:1094px;font-size:7.5px}

.side-share{left:41px;top:809px;width:22px}
.side-share span{display:block;height:22px;background:var(--grey);border-bottom:1px solid #777;
  color:var(--white);font-family:"Arimo",sans-serif;font-weight:700;font-size:6px;line-height:22px;text-align:center}

.chat-tab{left:731px;top:1006px;width:23px;height:66px;background:var(--orange);border-radius:6px 0 0 6px}
.chat-tab span{position:absolute;left:3px;top:38px;transform:rotate(-90deg);transform-origin:left top;color:var(--white);font-family:"Montserrat",sans-serif;font-weight:700;font-size:11px}
.chat-dot{left:738px;top:1050px;width:11px;height:11px;border-radius:50%;background:#8cc63f}
.to-top{left:716px;top:1114px;width:31px;height:31px;border-radius:50%;background:var(--orange);box-shadow:1px 2px 2px rgba(0,0,0,.3)}
.footer-accent{left:41px;top:1152px;width:713px;height:9px;background:var(--orange)}
.footer-bar{left:41px;top:1161px;width:713px;height:28px;background:var(--ink)}
</style>
</head>
<body>

<!-- hero -->
<div class="abs hero-photo" role="img" aria-label="Hands holding glowing cloud computing icons, devices and server racks on a dark blue background"></div>
<div class="abs brand"><span class="brand-mark"></span><span class="brand-name">BRELLOMINT</span></div>
<div class="abs account"><span>Login</span><span>|</span><span>Signup</span></div>
<h1 class="abs hero-title">Impartial<br>Cloud<br>Solutions</h1>
<p class="abs hero-sub">We provide impartial advice on cloud<br>solutions ensuring it's always right for you.</p>
<div class="abs hero-cta">Book a FREE Consultation</div>

<!-- navigation -->
<nav class="abs main-nav"></nav>
<span class="abs nav-item" style="left:129px">About Us</span>
<span class="abs nav-item" style="left:203px">Speciality</span>
<span class="abs nav-item" style="left:273px">Solutions</span>
<span class="abs nav-item" style="left:342px">Companies</span>
<span class="abs nav-item" style="left:421px">Testimonials</span>
<span class="abs nav-item" style="left:503px">FAQs</span>
<span class="abs nav-item" style="left:549px">Contact Us</span>
<span class="abs nav-search">Search</span>

<!-- testimonial -->
<div class="abs testimonial-photo" role="img" aria-label="Faded photo of a hand touching a tablet with network icons"></div>
<div class="abs client-badge">Quillmark Labs</div>
<svg class="abs quote-arrow" style="left:135px" width="30" height="30" viewBox="0 0 30 30" aria-hidden="true">
  <path d="M15 1 L29 15 L15 29 L1 15 Z" fill="none" stroke="var(--orange)" stroke-width="1.3"/>
  <path d="M21 15 H9 M12 12 L9 15 L12 18" fill="none" stroke="var(--orange-deep)" stroke-width="1.2"/>
</svg>
<svg class="abs quote-arrow" style="left:616px" width="30" height="30" viewBox="0 0 30 30" aria-hidden="true">
  <path d="M15 1 L29 15 L15 29 L1 15 Z" fill="none" stroke="var(--orange)" stroke-width="1.3"/>
  <path d="M9 15 H21 M18 12 L21 15 L18 18" fill="none" stroke="var(--orange-deep)" stroke-width="1.2"/>
</svg>
<p class="abs quote">"We were looking for a package that would be user friendly and suite our needs, we found that in Ledgerly. We were concerned with the well indeed. Maren is a dependable and knowledgeable person in this minefield of accounting software. Highly recommended." - Tomas Reddick</p>

<!-- about -->
<h2 class="abs section-title" style="top:465px;font-weight:400">About Us</h2>

<div class="abs about-block" style="left:105px;top:502px">
  <h3>Who we Are</h3>
  <p>Lorem Ipsum is simply dummy text of the printing and typesetting industry. Lorem Ipsum has been the industry's standard dummy ...</p>
  <span class="read-more">Read More</span>
</div>
<div class="abs about-block" style="left:105px;top:601px">
  <h3>Our Expertise</h3>
  <p>Lorem Ipsum is simply dummy text of the printing and typesetting industry. Lorem Ipsum has been the industry's standard dummy ...</p>
  <span class="read-more">Read More</span>
</div>
<div class="abs about-block" style="left:518px;top:502px">
  <h3>Our Team</h3>
  <p>Lorem Ipsum is simply dummy text of the printing and typesetting industry. Lorem Ipsum has been the industry's standard dummy ...</p>
  <span class="read-more">Read More</span>
</div>
<div class="abs about-block" style="left:519px;top:604px">
  <h3>Our Clients</h3>
  <p>Lorem Ipsum is simply dummy text of the printing and typesetting industry. Lorem Ipsum has been the industry's standard dummy ...</p>
  <span class="read-more">Read More</span>
</div>

<svg class="abs" style="left:334px;top:518px" width="130" height="68" viewBox="0 0 130 68" aria-hidden="true">
  <path d="M8 68 C-4 60 -2 38 18 36 C22 22 38 18 48 24 C54 4 84 -2 94 18 C104 12 120 18 118 34 C134 42 132 62 122 68 Z" fill="var(--grey-light)"/>
</svg>

<div class="abs about-cta"><span class="soft">BOOK A </span><span class="dark">FREE</span><br>CONSULTATION</div>

<!-- promo banner -->
<div class="abs promo" role="img" aria-label="Faded photo of a woman holding a laptop"></div>
<h2 class="abs promo-title">NOW, WE’VE MADE IT POSSIBLE FOR YOU</h2>
<p class="abs promo-sub">All Accounting needs are no longer a pain to you, we will help convert your current system to a simpler, flexible and one that responds to your needs accordingly</p>

<!-- contact -->
<div class="abs world-map" role="img" aria-label="Faint grey world map"></div>
<h2 class="abs section-title" style="top:794px;font-weight:400">Contact Us</h2>

<div class="abs field" style="top:840px;height:26px">Enter your Name</div>
<div class="abs field" style="top:872px;height:26px">Enter your email</div>
<div class="abs field" style="top:905px;height:120px">Enter your question</div>
<span class="abs copy-check"></span>
<span class="abs copy-label">Email me a copy of this e-mail</span>
<div class="abs send">Send</div>

<div class="abs divider"></div>

<svg class="abs" style="left:456px;top:887px" width="16" height="26" viewBox="0 0 16 26" aria-hidden="true">
  <path d="M8 26 C3 16 0 12 0 8 A8 8 0 0 1 16 8 C16 12 13 16 8 26 Z" fill="var(--orange)"/>
  <circle cx="8" cy="8" r="3.5" fill="var(--white)"/>
</svg>
<svg class="abs" style="left:456px;top:924px" width="20" height="14" viewBox="0 0 20 14" aria-hidden="true">
  <rect x="0.5" y="0.5" width="19" height="13" fill="none" stroke="var(--orange)"/>
  <path d="M0.5 0.5 L10 8 L19.5 0.5 M0.5 13.5 L7 6.5 M19.5 13.5 L13 6.5" fill="none" stroke="var(--orange)"/>
</svg>
<div class="abs contact-info">Melbourne, Victoria<br>1300 555 018<br>info@brellomint.com.au</div>

<span class="abs social-link large" style="left:452px">Share</span>
<span class="abs social-link large" style="left:502px">Post</span>
<span class="abs social-link large" style="left:550px">Link</span>
<span class="abs social-link large" style="left:597px">Plus</span>
<span class="abs social-link large" style="left:651px">Feed</span>

<span class="abs social-link small" style="left:578px">Share</span>
<span class="abs social-link small" style="left:602px">Post</span>
<span class="abs social-link small" style="left:623px">Link</span>
<span class="abs social-link small" style="left:643px">Plus</span>
<span class="abs social-link small" style="left:665px">Feed</span>

<!-- floating side share bar -->
<div class="abs side-share">
  <span>Share</span><span>Post</span><span>Link</span><span>Plus</span><span>Feed</span>
</div>

<div class="abs chat-tab"><span>chat</span></div>
<span class="abs chat-dot"></span>

<div class="abs to-top"></div>
<svg class="abs" style="left:721px;top:1121px" width="21" height="17" viewBox="0 0 21 17" aria-hidden="true">
  <path d="M2 9 L10.5 3 L19 9 M2 15 L10.5 9 L19 15" fill="none" stroke="var(--white)" stroke-width="2.6" stroke-linecap="round"/>
</svg>

<!-- footer -->
<div class="abs footer-accent"></div>
<footer class="abs footer-bar"></footer>

</body>
</html>
```